今回のチラシは当社が年4回発行している会報誌に同梱し、DMで直接お客様へ届けるものになります。
対象は庭付一戸建てに住まわれているお客様がほとんどです。なので、セールスワード(安い、お得、今だけ、限定、キャンペーンなど)をちりばめたようなギラギラしたチラシではなく、当社がお客様のお悩みから解放します的な心情に訴えるチラシにしたいです。
お客様のお困りの原因としては、お勤めでなかなか草むしりする時間が取れない、少し前までは自分でやっていたが年で体力的に難しくなった、奥様がマメに手入れしていたが他界してしまい手つかず状態、親が他界して家を相続したが自分は庭に興味なし。お隣さんから苦情が来てしまう。などなど様々です。
庭木が無くても雑草で困っている方にも、気兼ねなく当社にご依頼してもらえるようなイメージのチラシにしたいです。

トップページ
https://www.574k.co.jp/
除草
https://www.574k.co.jp/weeding/
砂利敷き(防草シート含む)
https://www.574k.co.jp/gravel/
表面:キャッチコピー、キャッチコピーに合う写真などの組合せ※情報はこの2つにしてシンプルに。
裏面:社名、支払い方法、フリーダイヤル、URL、QRコードなど ※添付資料参照
A4
両面
シンプル 複雑
単色 カラフル
暗い 明るい
日常 高級
遊び心 厳粛
未来的 伝統的
女性的 男性的
黄・オレンジ系、緑系、茶系
• イラストレーター形式 (.ai)
印刷用のPDFも納品ください。

情報量を少なくしシンプルにまとまっている。
お客様のお困りごとを端的に示していて伝わりやすい。
裏面にある商品説明の記載内容は必要十分の情報量で綺麗に整理されていて読みやすい。

皆様、この度は弊社のチラシ作成に応募いただき誠にありがとうございました。
社内で投票を行いましたが、どれかに集中することなく票がばらける程どれも良い感じだったと思います。
またチラシ作成やその他で募集させていただく際は是非ご応募ください。

```html
<!DOCTYPE html>
<html lang="ja">
<head>
<meta charset="UTF-8">
<title>雑草の問題を解決します</title>
<link href="https://fonts.googleapis.com/css2?family=M+PLUS+Rounded+1c:wght@500;700;800&family=Zen+Maru+Gothic:wght@500;700&display=swap" rel="stylesheet">
<style>
  :root {
    --green: #4f9a3c;
    --green-dark: #2f6e2a;
    --leaf: #a6d43a;
    --yellow: #f2e03a;
    --white: #ffffff;
    --ink: #2c5b27;
    --muted: #555555;
  }
  * { margin: 0; padding: 0; box-sizing: border-box; }
  html, body { width: 846px; height: 1200px; overflow: hidden; background: var(--white); }
  body { font-family: "M PLUS Rounded 1c", "Zen Maru Gothic", sans-serif; }
  .flyer { position: relative; width: 846px; height: 1200px; overflow: hidden; background: var(--white); }

  .garden-photo {
    position: absolute; left: 0; top: 0; width: 846px; height: 670px;
    background:
      linear-gradient(90deg, #2d4a24 0%, #4e6e35 30%, #6f7a52 48%, #5b7f3e 60%, #3f6a2e 80%, #8a8d74 100%);
  }
  .garden-photo::after {
    content: ""; position: absolute; left: 423px; right: 0; bottom: 0; height: 300px;
    background: linear-gradient(180deg, rgba(120,100,70,0) 0%, rgba(120,98,70,0.7) 100%);
  }

  .headline-panel {
    position: absolute; left: 150px; top: 0; width: 546px; height: 266px;
    background: rgba(20, 35, 20, 0.62);
    text-align: center; color: var(--white);
  }
  .headline-lead {
    display: inline-block; margin-top: 14px; padding: 4px 26px;
    background: var(--green); border-radius: 6px;
    font-size: 27px; font-weight: 700; letter-spacing: 2px;
  }
  .headline-impact {
    display: inline-block; margin-top: 12px; padding: 0 14px;
    background: var(--green); color: var(--yellow);
    font-size: 38px; font-weight: 800; letter-spacing: 4px; line-height: 52px;
  }
  .headline-main {
    margin-top: 4px; color: var(--leaf);
    font-size: 64px; font-weight: 800; letter-spacing: 3px; line-height: 76px;
  }
  .headline-tail { font-size: 32px; font-weight: 700; letter-spacing: 2px; }

  .compare-label {
    position: absolute; top: 586px; color: var(--white);
    font-family: "Zen Maru Gothic", sans-serif; font-size: 52px; font-weight: 500;
  }
  .compare-label.before { left: 34px; }
  .compare-label.after { left: 626px; }
  .compare-arrow { position: absolute; left: 300px; top: 588px; }

  .question {
    position: absolute; left: 52px; top: 690px;
    font-size: 22px; font-weight: 500; color: var(--muted);
    padding-left: 42px;
  }
  .question::before {
    content: ""; position: absolute; left: 0; top: 12px; width: 30px; height: 6px; background: var(--yellow);
  }

  .concerns { position: absolute; left: 52px; top: 740px; width: 560px; list-style: none; }
  .concern {
    position: relative; padding-left: 56px; margin-bottom: 22px;
    font-size: 32px; font-weight: 800; color: var(--ink); line-height: 42px;
  }
  .concern svg { position: absolute; left: 0; top: 4px; }

  .worker-illustration {
    position: absolute; left: 620px; top: 800px; width: 200px; height: 280px;
    background: linear-gradient(180deg, #e4f0d8 0%, #9ccc7c 100%);
    border-radius: 100px 100px 0 0;
  }

  .closing-band {
    position: absolute; left: 0; bottom: 0; width: 846px; height: 112px;
    background: var(--green);
    display: flex; align-items: center; justify-content: center;
    color: var(--white); font-size: 34px; font-weight: 800; letter-spacing: 1px;
  }
</style>
</head>
<body>
<main class="flyer">
  <div class="garden-photo" role="img" aria-label="雑草に覆われた庭と、除草後に土が見えるようになった庭の比較写真"></div>

  <header class="headline-panel">
    <p class="headline-lead">雑草の問題を解決します</p><br>
    <p class="headline-impact">衝撃的</p>
    <h1 class="headline-main">ビフォーアフター</h1>
    <p class="headline-tail">をご覧ください！</p>
  </header>

  <span class="compare-label before">Before</span>
  <svg class="compare-arrow" width="180" height="60" viewBox="0 0 180 60" aria-hidden="true">
    <rect x="0" y="22" width="130" height="16" fill="#ffffff"/>
    <polygon points="126,4 176,30 126,56" fill="#ffffff"/>
  </svg>
  <span class="compare-label after">After</span>

  <p class="question">以下のようなご状況はございますか？</p>

  <ul class="concerns">
    <li class="concern">
      <svg width="38" height="38" viewBox="0 0 38 38" aria-hidden="true"><rect x="3" y="5" width="28" height="28" rx="3" fill="none" stroke="#4f9a3c" stroke-width="3.5"/><path d="M9 18 L17 26 L35 4" fill="none" stroke="#4f9a3c" stroke-width="5" stroke-linecap="round" stroke-linejoin="round"/></svg>
      草むしりする時間がなく庭が雑草だらけ
    </li>
    <li class="concern">
      <svg width="38" height="38" viewBox="0 0 38 38" aria-hidden="true"><rect x="3" y="5" width="28" height="28" rx="3" fill="none" stroke="#4f9a3c" stroke-width="3.5"/><path d="M9 18 L17 26 L35 4" fill="none" stroke="#4f9a3c" stroke-width="5" stroke-linecap="round" stroke-linejoin="round"/></svg>
      草むしりが体力的に厳しい
    </li>
    <li class="concern">
      <svg width="38" height="38" viewBox="0 0 38 38" aria-hidden="true"><rect x="3" y="5" width="28" height="28" rx="3" fill="none" stroke="#4f9a3c" stroke-width="3.5"/><path d="M9 18 L17 26 L35 4" fill="none" stroke="#4f9a3c" stroke-width="5" stroke-linecap="round" stroke-linejoin="round"/></svg>
      今まで手入れをしていた人が<br>手入れできなくなった
    </li>
    <li class="concern">
      <svg width="38" height="38" viewBox="0 0 38 38" aria-hidden="true"><rect x="3" y="5" width="28" height="28" rx="3" fill="none" stroke="#4f9a3c" stroke-width="3.5"/><path d="M9 18 L17 26 L35 4" fill="none" stroke="#4f9a3c" stroke-width="5" stroke-linecap="round" stroke-linejoin="round"/></svg>
      近所から苦情が来てしまう
    </li>
  </ul>

  <div class="worker-illustration" role="img" aria-label="緑の帽子と作業着姿で指を立てて案内するスタッフのイラスト"></div>

  <footer class="closing-band">雑草のことでお困りでしたら私たちが解決します！</footer>
</main>
</body>
</html>
```